Lumentide

We have already had a logo designed. Attached is the logo.
We are now wanting to design a label that will wrap around a plastic bottle which contains 1 litre of fluid. The size of the label is 15cm high by 28 cm wide.
The bottle for which the label will be used is a natural wellbeing supplement in a class of its own. It is a liquid tonic/complementary medicine - not a drink you guzzle down like zestorade.
The label needs to look natural and healthy and include the logo attached.
This is a premium bottle which will cost more than $50 AUD per bottle. The label needs to be classy as you would expect to find on an expensive bottle of wine.
The label needs to be able to sell the bottle and it needs to convince that what is inside the bottle is worth what it will cost.
The product does not have fruit in it and is not a water drink. One of the ingredients is an extract from the French Maritime Pine Bark.
We do not want the label to be to busy.
The product is to market in China, United States and Australia.
We will have to typeset certain wording onto the label - Ingredients, company details, bottle code etc which will be on the back of the bottle.
Updates

We have uploaded a picture of the plastic bottle that the label will be used on. The dimensions of the label have been included in the project brief.

Regards

Reason: We realise that the time period allowed to create a label may have been to short for some designers. Thanks

Reason: Just waiting on final designs to be submitted. This will be the last extension. Regards

Target Market(s)

Generally adults aged 35 to 65.

Industry/Entity Type

Plastic

Requirements
Must have
• Most of this information has been outlined above.

```html
<!DOCTYPE html>
<html lang="en">
<head>
<meta charset="utf-8">
<title>Lumentide – health and wellbeing drink label</title>
<link rel="stylesheet" href="https://fonts.googleapis.com/css2?family=Comfortaa:wght@300;400;700&display=swap">
<style>
  :root {
    --backdrop: #e8e8ea;
    --label-white: #fbfbfb;
    --brand-green: #1f6b2c;
    --lime: #8dbb2a;
    --plum: #8e1f6e;
    --fine-ink: #8a8a8a;
    --lime-ink: #2f2f2f;
    --plum-ink: #f6e4f0;
    --panel-highlight: #ffffff;
  }
  * { box-sizing: border-box; margin: 0; padding: 0; }
  html, body {
    width: 940px; height: 1200px; overflow: hidden;
    background: var(--backdrop);
    font-family: "Comfortaa", sans-serif;
  }
  .canvas {
    position: relative; width: 940px; height: 1200px;
    display: flex; justify-content: center; align-items: center; gap: 24px;
  }
  .label {
    position: relative; width: 290px; height: 720px;
    background: var(--label-white);
    box-shadow: 0 2px 10px rgba(0,0,0,0.08);
    display: flex; flex-direction: column; align-items: center;
  }
  .label--back { width: 250px; align-items: flex-start; padding: 70px 26px 0; }
  .back-info { display: flex; flex-direction: column; gap: 10px; }
  .back-info p { font-size: 10px; line-height: 1.5; color: var(--fine-ink); }
  .recycle-mark {
    position: absolute; left: 26px; bottom: 40px;
    width: 16px; height: 16px; border-radius: 50%;
    border: 2px solid var(--fine-ink);
  }
  .brand {
    margin-top: 150px;
    font-weight: 700; font-size: 34px; letter-spacing: -0.5px;
    color: var(--brand-green);
  }
  .tree-art {
    margin-top: 22px; width: 170px; height: 190px;
    border-radius: 45% 45% 8% 8%;
    background: radial-gradient(circle at 50% 40%, #bcd89a 0%, #dcebc8 55%, var(--label-white) 80%);
  }
  .flavour-panel {
    margin-top: 10px; width: 250px; height: 190px;
    border-radius: 14px;
    padding: 22px 0 0;
    text-align: center;
  }
  .flavour-panel--lime { background: var(--lime); color: var(--lime-ink); }
  .flavour-panel--plum { background: var(--plum); color: var(--plum-ink); }
  .tagline { font-weight: 300; font-size: 26px; line-height: 0.95; }
  .product-type {
    font-weight: 700; font-size: 40px; line-height: 1.1; color: var(--panel-highlight);
  }
  .volume {
    font-weight: 700; font-size: 13px; letter-spacing: 1px; word-spacing: 8px;
    color: var(--panel-highlight);
  }
</style>
</head>
<body>
<main class="canvas">
  <section class="label label--back" aria-label="Back of label">
    <div class="back-info">
      <p>Ingredients: purified water, pine bark extract, natural flavours.</p>
      <p>Shake well before use. Store in a cool dry place.</p>
      <p>Nutrition information per 30 ml serve</p>
      <p>Energy 12 kJ<br>Sugars 0.4 g</p>
      <p>Best before: see cap</p>
    </div>
    <span class="recycle-mark"></span>
  </section>

  <section class="label label--front" aria-label="Front of label, green variant">
    <h1 class="brand">Lumentide</h1>
    <div class="tree-art" role="img" aria-label="Line drawing of a young tree with green leaves"></div>
    <div class="flavour-panel flavour-panel--lime">
      <p class="tagline">health<br>and<br>wellbeing</p>
      <p class="product-type">drink</p>
      <p class="volume">1 LITRE</p>
    </div>
  </section>

  <section class="label label--front" aria-label="Front of label, purple variant">
    <h2 class="brand">Lumentide</h2>
    <div class="tree-art" role="img" aria-label="Line drawing of a young tree with green leaves"></div>
    <div class="flavour-panel flavour-panel--plum">
      <p class="tagline">health<br>and<br>wellbeing</p>
      <p class="product-type">drink</p>
      <p class="volume">1 LITRE</p>
    </div>
  </section>
</main>
</body>
</html>
```